Food label for BarBQ sauce and creole seasoning under the name HONEY BAYOU

I need a label design using the name "HONEY BAYOU" that will be used on bottles of Bar B Q sauce, both Creole and Cajun, and dry Cajun and dry Creole seasoning. I have attached a copy of the letter style we will be using. It is NOT a religious product or has any religious meaning. It comes from a saying old southerners used when they tasted something special -"Oh Honey Bayou". The labels for the Bar B Q sauces will be 5" wide by 3" tall, and the dry seasonings will be 5" wide by 3 1/2" tall. The products will that they are from South Louisiana and should reflect the typical food from the New Orleans area. This produce name is a REGISTERED TRADE NAME with the US trademark office.

```html
<!DOCTYPE html>
<html lang="en">
<head>
<meta charset="utf-8">
<title>Honey Bayou Bar B Q Sauce Label</title>
<link href="https://fonts.googleapis.com/css2?family=Gochi+Hand&family=Open+Sans:wght@400&display=swap" rel="stylesheet">
<style>
  :root {
    --stage: #cf5528;
    --label-edge: #7d0c12;
    --label-mid: #cf2f1a;
    --label-glow: #f39a22;
    --label-core: #fbc33a;
    --art-dark: #4a1410;
    --art-flame: #f26a1b;
    --ink-light: #ffffff;
    --ink-shadow: rgba(90, 10, 5, 0.55);
  }
  * { margin: 0; padding: 0; box-sizing: border-box; }
  html, body {
    width: 1200px;
    height: 800px;
    overflow: hidden;
    background: var(--stage);
  }
  .canvas {
    position: relative;
    width: 1200px;
    height: 800px;
    display: flex;
    align-items: center;
    justify-content: center;
  }
  .label {
    position: relative;
    width: 1000px;
    height: 700px;
    background: radial-gradient(ellipse 60% 62% at 50% 48%,
      var(--label-core) 0%,
      var(--label-glow) 28%,
      var(--label-mid) 62%,
      var(--label-edge) 100%);
    overflow: hidden;
  }
  .label__art {
    position: absolute;
    left: 258px;
    top: 125px;
    width: 494px;
    height: 253px;
    border-radius: 120px 120px 40px 40px;
    background: radial-gradient(ellipse at 50% 40%,
      var(--art-flame) 0%,
      #c0391a 55%,
      var(--art-dark) 100%);
  }
  .label__title {
    position: absolute;
    left: 0;
    right: 0;
    top: 372px;
    text-align: center;
    font-family: "Gochi Hand", cursive;
    font-size: 104px;
    line-height: 1;
    letter-spacing: 3px;
    text-transform: uppercase;
    color: var(--ink-light);
    text-shadow: 0 3px 6px var(--ink-shadow);
  }
  .label__product {
    position: absolute;
    left: 0;
    right: 0;
    top: 482px;
    text-align: center;
    font-family: "Gochi Hand", cursive;
    font-size: 68px;
    line-height: 1;
    letter-spacing: 2px;
    text-transform: uppercase;
    color: var(--ink-light);
    text-shadow: 0 3px 6px var(--ink-shadow);
  }
  .label__blurb {
    position: absolute;
    left: 320px;
    width: 360px;
    top: 560px;
    text-align: center;
    font-family: "Open Sans", sans-serif;
    font-size: 12.5px;
    line-height: 1.35;
    color: var(--ink-light);
  }
</style>
</head>
<body>
  <main class="canvas">
    <section class="label">
      <div class="label__art" role="img" aria-label="Illustration of a flaming barbecue grill with a crossed sausage fork and spatula"></div>
      <h1 class="label__title">Honey Bayou</h1>
      <p class="label__product">Bar B Q Sauce</p>
      <p class="label__blurb">Slow simmered in small batches with cane sugar, smoked paprika and Creole spices from South Louisiana kitchens. Brush on ribs, chicken and sausage for a sweet finish.</p>
    </section>
  </main>
</body>
</html>
```